REAL ESTATE MAILBOX DROP FLYER

I am looking for two flyer designs. One for DL and one for A4 size. My company is a boutique real estate agency that offers a full/high quality service at a very low commission rate.

Key Phrases to be included

A4 Design should have a space for some text and a table in the center (outline below)

Target Market(s)

Home Owners

Industry/Entity Type

Real Estate Agent

Colors
0455a3

Requirements
Must have
• Eye Catching
• Bold
• high end feel
• Color pallette should match the logo
• The feel of the brochures must convey a trustworthy, high end service.
• Must be eye catching and easy to read
• Editable file formats must be supplied

```html
<!DOCTYPE html>
<html lang="en">
<head>
<meta charset="utf-8">
<title>Harbourline Property – Mailbox Flyer</title>
<link href="https://fonts.googleapis.com/css2?family=Cinzel:wght@600;700&family=Montserrat:wght@500;700;800&display=swap" rel="stylesheet">
<style>
  :root {
    --navy: #0c2b4a;
    --navy-soft: #3f5f7d;
    --white: #ffffff;
    --grey-band: #a9abad;
    --backdrop: #e4e4e4;
    --divider: #c9cbce;
  }
  * { margin: 0; padding: 0; box-sizing: border-box; }
  html, body {
    width: 1200px; height: 1200px; overflow: hidden;
    background: var(--backdrop);
  }
  .flyer {
    position: absolute; left: 200px; top: 35px;
    width: 800px; height: 1130px;
    background: var(--white);
    overflow: hidden;
    box-shadow: 0 6px 24px rgba(0,0,0,0.18);
    font-family: 'Montserrat', sans-serif;
    color: var(--navy);
  }
  .flyer-shapes { position: absolute; inset: 0; }
  .brand-name {
    position: absolute; top: 58px; left: 0; width: 800px;
    text-align: center;
    font-family: 'Cinzel', serif; font-weight: 700;
    font-size: 34px; letter-spacing: 1px; line-height: 1.1;
    color: var(--navy);
  }
  .offer {
    position: absolute; left: 250px; top: 410px; width: 300px;
    text-align: center; color: var(--white);
    font-family: 'Cinzel', serif; font-weight: 700;
  }
  .offer-full { font-size: 30px; line-height: 1; }
  .offer-service { font-size: 25px; margin-top: 14px; line-height: 1; }
  .offer-rate { display: flex; align-items: center; justify-content: center; gap: 8px; margin-top: 8px; }
  .offer-percent { font-size: 56px; line-height: 1; }
  .offer-commission { font-size: 23px; line-height: 1; }
  .contact-banner {
    position: absolute; left: 130px; top: 702px; width: 540px; height: 46px;
    display: flex; align-items: center; justify-content: center;
    font-family: 'Cinzel', serif; font-weight: 700; font-size: 22px;
    color: var(--white); letter-spacing: 0.5px;
  }
  .cta { position: absolute; left: 0; width: 800px; text-align: center; }
  .cta-phone { top: 760px; font-size: 44px; font-weight: 800; }
  .cta-appraisal { top: 818px; font-size: 46px; font-weight: 800; }
  .cta-appraisal .cta-lead { font-size: 38px; }
  .cta-saving { top: 878px; font-size: 21px; font-weight: 500; }
  .contact-details { position: absolute; left: 40px; top: 940px; width: 440px; }
  .contact-heading { font-size: 21px; font-weight: 700; margin-bottom: 10px; }
  .contact-row { display: flex; align-items: center; gap: 12px; height: 34px; }
  .contact-row svg { width: 26px; height: 26px; flex: none; }
  .contact-name { font-size: 21px; font-weight: 700; }
  .contact-text { font-size: 18.5px; font-weight: 500; }
  .column-divider {
    position: absolute; left: 495px; top: 925px; width: 2px; height: 135px;
    background: var(--divider);
  }
  .tagline {
    position: absolute; left: 505px; top: 950px; width: 295px;
    text-align: center; font-size: 31px; font-weight: 800; line-height: 1.3;
  }
</style>
</head>
<body>
<main class="flyer">
  <svg class="flyer-shapes" viewBox="0 0 800 1130" width="800" height="1130">
    <defs>
      <linearGradient id="photo-living-top" x1="0" y1="0" x2="0" y2="1">
        <stop offset="0" stop-color="#f2f2f1"/>
        <stop offset="0.55" stop-color="#d6d5d2"/>
        <stop offset="1" stop-color="#b9b8b5"/>
      </linearGradient>
      <linearGradient id="photo-bedroom" x1="0" y1="0" x2="0" y2="1">
        <stop offset="0" stop-color="#e9eaeb"/>
        <stop offset="0.6" stop-color="#c4c7cc"/>
        <stop offset="1" stop-color="#5e5f63"/>
      </linearGradient>
      <linearGradient id="photo-lounge" x1="0" y1="0" x2="0" y2="1">
        <stop offset="0" stop-color="#eceef0"/>
        <stop offset="0.55" stop-color="#d9d7d2"/>
        <stop offset="1" stop-color="#b08a60"/>
      </linearGradient>
      <linearGradient id="banner-fade" x1="0" y1="0" x2="1" y2="0">
        <stop offset="0" stop-color="#0c2b4a"/>
        <stop offset="0.65" stop-color="#143758"/>
        <stop offset="1" stop-color="#5c7893"/>
      </linearGradient>
    </defs>

    <rect class="photo-top" x="0" y="0" width="800" height="600" fill="url(#photo-living-top)" role="img" aria-label="Photo of a bright open-plan living and dining room with grey sofas"/>
    <polygon class="photo-left" points="0,570 250,420 250,680 0,830" fill="url(#photo-bedroom)" role="img" aria-label="Photo of a styled bedroom with white bedding"/>
    <polygon class="photo-right" points="800,570 550,420 550,680 800,830" fill="url(#photo-lounge)" role="img" aria-label="Photo of a lounge room with white sofa and coffee tables"/>

    <polyline points="0,570 250,420 400,330 550,420 800,570" fill="none" stroke="#ffffff" stroke-width="9"/>
    <polygon class="offer-panel" points="250,420 400,330 550,420 550,680 400,590 250,680" fill="var(--navy)" stroke="#ffffff" stroke-width="9" stroke-linejoin="miter"/>
    <polygon class="info-area" points="0,830 400,590 800,830 800,1130 0,1130" fill="#ffffff"/>

    <polygon class="banner-shape" points="130,748 185,702 615,702 670,748" fill="url(#banner-fade)"/>

    <rect class="footer-band" x="0" y="1088" width="800" height="42" fill="var(--grey-band)"/>
    <polygon class="footer-tab" points="210,1130 250,1092 590,1092 630,1130" fill="var(--navy)"/>
  </svg>

  <div class="brand-name">HARBOURLINE<br>PROPERTY</div>

  <div class="offer">
    <div class="offer-full">FULL</div>
    <div class="offer-service">SERVICE AGENCY</div>
    <div class="offer-rate">
      <span class="offer-percent">1%</span>
      <span class="offer-commission">COMMISSION</span>
    </div>
  </div>

  <div class="contact-banner">CONTACT MARCUS TODAY ON</div>

  <div class="cta cta-phone">0412-000-318</div>
  <div class="cta cta-appraisal"><span class="cta-lead">FOR A</span> FREE APPRAISAL!</div>
  <div class="cta cta-saving">Save Thousands On Commissions!</div>

  <section class="contact-details">
    <div class="contact-heading">CONTACT DETAILS</div>
    <div class="contact-row">
      <svg viewBox="0 0 26 26" aria-hidden="true">
        <circle cx="13" cy="13" r="11.5" fill="none" stroke="#0c2b4a" stroke-width="2"/>
        <path d="M9 7.5c-1 .6-1.6 1.6-1.2 3 .9 3.2 3.5 6 6.7 7.3 1.3.5 2.4 0 3.1-1l.4-.7-2.6-1.8-1.2 1.1c-1.6-.8-2.8-2-3.6-3.7l1.1-1.2L10 7z" fill="#0c2b4a"/>
      </svg>
      <span class="contact-name">MARCUS BELL-0412 000 318</span>
    </div>
    <div class="contact-row">
      <svg viewBox="0 0 26 26" aria-hidden="true">
        <rect x="2" y="6" width="22" height="15" fill="none" stroke="#0c2b4a" stroke-width="2"/>
        <polyline points="2,6 13,15 24,6" fill="none" stroke="#0c2b4a" stroke-width="2"/>
      </svg>
      <span class="contact-text">marcus@harbourlineproperty.com.au</span>
    </div>
    <div class="contact-row">
      <svg viewBox="0 0 26 26" aria-hidden="true">
        <circle cx="13" cy="13" r="11" fill="none" stroke="#0c2b4a" stroke-width="2"/>
        <ellipse cx="13" cy="13" rx="5" ry="11" fill="none" stroke="#0c2b4a" stroke-width="1.6"/>
        <line x1="2" y1="13" x2="24" y2="13" stroke="#0c2b4a" stroke-width="1.6"/>
        <line x1="4" y1="7.5" x2="22" y2="7.5" stroke="#0c2b4a" stroke-width="1.4"/>
        <line x1="4" y1="18.5" x2="22" y2="18.5" stroke="#0c2b4a" stroke-width="1.4"/>
      </svg>
      <span class="contact-text">www.harbourlineproperty.com.au</span>
    </div>
  </section>

  <div class="column-divider"></div>
  <div class="tagline">MORE MONEY<br>IN YOUR POCKET!</div>
</main>
</body>
</html>
```